Business card for partnership

Plumbing and hvac company needing a minimal business card. We already have a logo i would like the front of the card just the logo and the back have all info.

Target Market(s)

Commercial facilities

Industry/Entity Type

Plumbing hvac

Contact Information for Business Card

We would like it double sided. Logo big and bold on the front and out info on the back. Our info on back would be name and position phone, email, and location

```html
<!DOCTYPE html>
<html lang="en">
<head>
<meta charset="UTF-8">
<title>Ridgeline Mechanical – Business Card</title>
<link rel="stylesheet" href="https://fonts.googleapis.com/css2?family=Arimo:wght@400;700&display=swap">
<style>
  :root {
    --stage: #2b2b2b;
    --card-black: #0a0a0a;
    --card-orange: #f07f36;
    --ink-white: #ffffff;
    --accent-orange: #f07f36;
  }
  * { margin: 0; padding: 0; box-sizing: border-box; }
  html, body { width: 1200px; height: 1015px; overflow: hidden; }
  body {
    background: var(--stage);
    font-family: "Arimo", Arial, sans-serif;
    color: var(--ink-white);
    position: relative;
  }
  .card {
    position: absolute;
    width: 580px;
    height: 331px;
  }
  .card-front {
    left: 110px;
    top: 150px;
    background: var(--card-black);
    display: flex;
    align-items: center;
    justify-content: center;
  }
  .card-back {
    left: 510px;
    top: 534px;
    background: var(--card-orange);
  }
  .wordmark {
    display: flex;
    align-items: center;
    gap: 12px;
  }
  .wordmark-mark {
    width: 34px;
    height: 34px;
    background: var(--accent-orange);
    flex: none;
  }
  .wordmark-text {
    font-weight: 700;
    line-height: 1;
    color: var(--ink-white);
  }
  .wordmark-text .line-main { display: block; letter-spacing: 1px; }
  .wordmark-text .line-sub { display: block; letter-spacing: 6px; }
  .card-front .wordmark-text .line-main { font-size: 54px; }
  .card-front .wordmark-text .line-sub { font-size: 22px; margin-top: 6px; }

  .card-back .wordmark {
    position: absolute;
    right: 46px;
    top: 66px;
  }
  .card-back .wordmark-mark { width: 20px; height: 20px; background: var(--ink-white); }
  .card-back .wordmark-text .line-main { font-size: 31px; }
  .card-back .wordmark-text .line-sub { font-size: 13px; letter-spacing: 3.5px; margin-top: 4px; }

  .contact {
    position: absolute;
    left: 48px;
    top: 92px;
  }
  .contact-name { font-size: 20px; font-weight: 700; letter-spacing: 0.5px; }
  .contact-role { font-size: 12px; letter-spacing: 1px; margin-top: 3px; }
  .contact-list { list-style: none; margin-top: 24px; font-size: 14px; }
  .contact-list li { display: flex; align-items: center; gap: 8px; margin-bottom: 5px; }
  .contact-list svg { width: 14px; height: 14px; flex: none; }
  .contact-address { font-size: 14px; line-height: 1.35; margin-top: 24px; }
</style>
</head>
<body>
  <section class="card card-front" aria-label="Card front">
    <div class="wordmark">
      <span class="wordmark-mark"></span>
      <span class="wordmark-text">
        <span class="line-main">RIDGELINE</span>
        <span class="line-sub">MECHANICAL</span>
      </span>
    </div>
  </section>

  <section class="card card-back" aria-label="Card back">
    <div class="contact">
      <p class="contact-name">DANIEL REYES</p>
      <p class="contact-role">MANAGING DIRECTOR</p>
      <ul class="contact-list">
        <li>
          <svg viewBox="0 0 24 24" fill="#fff"><path d="M6.6 10.8a15.1 15.1 0 0 0 6.6 6.6l2.2-2.2c.3-.3.7-.4 1-.2 1.1.4 2.3.6 3.6.6.6 0 1 .4 1 1V20c0 .6-.4 1-1 1A17 17 0 0 1 3 4c0-.6.4-1 1-1h3.5c.6 0 1 .4 1 1 0 1.3.2 2.5.6 3.6.1.3 0 .7-.2 1z"/></svg>
          044-555 010 222
        </li>
        <li>
          <svg viewBox="0 0 24 24" fill="#fff"><path d="M2 5h20v14H2z"/><path d="M2 5l10 8 10-8" fill="none" stroke="#f07f36" stroke-width="2"/></svg>
          info@ridgelinemech.com
        </li>
        <li>
          <svg viewBox="0 0 24 24" fill="none" stroke="#fff" stroke-width="2"><circle cx="12" cy="12" r="10"/><path d="M2 12h20M12 2c3 3 3 17 0 20M12 2c-3 3-3 17 0 20"/></svg>
          www.ridgelinemech.com
        </li>
      </ul>
      <p class="contact-address">421, Address line goes here<br>45452, Country Name</p>
    </div>
    <div class="wordmark">
      <span class="wordmark-mark"></span>
      <span class="wordmark-text">
        <span class="line-main">RIDGELINE</span>
        <span class="line-sub">MECHANICAL</span>
      </span>
    </div>
  </section>
</body>
</html>
```